Stylish High End Wedding Videography/Films Website (BDMR)

We need a modern and high-end website look for our wedding video and films business. We films weddings all over the United Kingdom and at European destinations so need something to reflect our work. The website should be visually stunning with images and videos being the focal point as this is what our services are;

I have uploads of some items I like and the features the site needs to have. These have been taken from other websites using standout features.

We need the following pages;

1 - Homepage
2 - Films Index Page
3 - Individual Films Page
4 - Prices / Collection Page
5 - Reviews
6 - Options
7 - About
8 - Contact
9 - Blog Index
10 - Blog Page

All pages must be consistent so have a similar style.

Pages on menu:
Films
Prices
Reviews
Options
About
Contact

We require a responsive look too. Over 90% of our visitors access the website via their mobile devices.

Please use the colours from our logo to incorporate into the website.

Target Market(s)

Wedding Couples

Industry/Entity Type

Wedding Photography

Number of Pages Required

5+ page

Font styles to use
Sans Serif
Script

Requirements
Must have
• The logo must be in the centre of the menu at the top.

Social icons at the bottom of the page.

Use only two fonts including Lore which is supplied
Nice to have
• Different video for each page on the top header. This will play behind the menu.

```html
<!DOCTYPE html>
<html lang="en">
<head>
<meta charset="utf-8">
<title>BDMR Wedding Films</title>
<link rel="stylesheet" href="https://fonts.googleapis.com/css2?family=Libre+Baskerville&family=Jost:wght@400;500&display=swap">
<style>
:root{
  --gold:#9d864c;
  --gold-soft:#b7a46f;
  --brown:#443a35;
  --footer:#3f3935;
  --ink:#2f2a27;
  --cream:#f3efe7;
  --mist:#e4e3e8;
  --white:#ffffff;
}
*{margin:0;padding:0;box-sizing:border-box}
html,body{width:1200px;height:3600px;overflow:hidden;background:var(--white)}
body{position:relative;font-family:"Jost",sans-serif;color:var(--ink)}
.serif{font-family:"Libre Baskerville",serif}
.abs{position:absolute}
.photo{position:absolute;display:block}

/* hero */
.hero{position:absolute;left:0;top:0;width:1200px;height:652px;
  background:linear-gradient(180deg,#2d3a22 0%,#4d5a32 35%,#6a6b4a 55%,#2e3427 80%,#3c3f34 100%)}
.hero-couple{left:390px;top:90px;width:420px;height:562px;
  background:linear-gradient(180deg,#8a7560 0%,#3c4968 45%,#e8e4dc 75%,#f4f2ee 100%);border-radius:160px 160px 0 0;opacity:.85}
.nav{position:absolute;top:40px;left:0;width:1200px;height:40px}
.nav a{position:absolute;top:0;color:var(--white);text-decoration:none;font-size:12.5px;letter-spacing:2px;font-weight:500}
.brand{position:absolute;left:500px;top:-14px;width:200px;text-align:center;color:var(--white);
  font-family:"Libre Baskerville",serif;font-size:22px;letter-spacing:6px}
.brand small{display:block;font-family:"Libre Baskerville",serif;font-size:8px;letter-spacing:4px;margin-top:2px}
.hero-title{position:absolute;left:395px;top:366px;width:411px;height:164px;background:rgba(60,52,48,.72)}
.hero-title .frame{position:absolute;left:13px;top:14px;right:13px;bottom:14px;border:1px solid rgba(255,255,255,.8)}
.hero-title h1{position:absolute;top:36px;width:100%;text-align:center;color:var(--white);font-weight:400;font-size:32px;letter-spacing:5px}
.hero-title p{position:absolute;top:82px;width:100%;text-align:center;color:var(--white);font-size:18px;letter-spacing:2.5px;line-height:26px}

/* intro */
.eyebrow{left:88px;top:712px;font-size:11px;letter-spacing:1.5px;line-height:17px}
.intro-h{left:126px;top:772px;color:var(--gold);font-size:28px;font-weight:400;letter-spacing:1.5px;line-height:32px}
.intro-p{left:126px;top:870px;width:262px;font-size:10.5px;letter-spacing:1.4px;line-height:19px;text-align:justify;text-transform:uppercase}
.btn{position:absolute;border:1.5px solid var(--gold);color:var(--gold);font-family:"Libre Baskerville",serif;font-size:12px;letter-spacing:1px;display:flex;align-items:center;justify-content:center;gap:8px}
.play{position:absolute;width:48px;height:48px;border:2px solid var(--white);border-radius:50%}
.play::after{content:"";position:absolute;left:19px;top:16px;border-left:11px solid var(--white);border-top:7px solid transparent;border-bottom:7px solid transparent}

/* grid */
.tile{position:absolute;width:300px;height:300px}
.feature{background:var(--gold-soft)}
.feature .frame{position:absolute;left:14px;top:14px;right:14px;bottom:14px;border:1.5px solid rgba(255,255,255,.85)}
.feature h3{position:absolute;top:110px;width:100%;text-align:center;color:var(--white);font-weight:400;font-size:28px;letter-spacing:2px}
.feature p{position:absolute;top:150px;width:100%;text-align:center;color:var(--white);font-family:"Libre Baskerville",serif;font-size:14px;letter-spacing:1px}

/* alternative */
.alt{position:absolute;left:0;top:1762px;width:1200px;height:585px;background:var(--brown)}
.section-h{position:absolute;width:1200px;text-align:center;color:var(--gold);font-weight:400;letter-spacing:1.5px}
.section-sub{position:absolute;width:1200px;text-align:center;color:var(--gold);font-size:10.5px;letter-spacing:2px;line-height:14px}
.card-name{position:absolute;color:var(--gold);font-family:"Libre Baskerville",serif;font-size:15px;letter-spacing:2px}
.card-place{position:absolute;color:#d8d0c4;font-size:10px;letter-spacing:1.2px}

/* reviews */
.review-tag{position:absolute;left:263px;top:2685px;width:187px;height:35px;background:var(--gold);color:var(--white);
  font-family:"Libre Baskerville",serif;font-size:15px;letter-spacing:2px;display:flex;align-items:center;justify-content:center}
.review-text{left:263px;top:2736px;width:673px;font-size:10.5px;letter-spacing:1.5px;line-height:19px;text-transform:uppercase;text-align:justify}
.dots{left:566px;top:2834px;display:flex;gap:11px}
.dots i{width:4px;height:4px;border-radius:50%;background:#d8d3cb}
.dots i:first-child{background:var(--ink)}

/* social feed */
.feed{position:absolute;left:0;top:2976px;width:1200px;height:225px;background:var(--mist)}
.feed h4{position:absolute;left:170px;top:38px;font-family:"Libre Baskerville",serif;font-weight:400;font-size:16px;color:var(--ink)}
.thumb{position:absolute;top:76px;width:101px;height:101px}

/* footer */
.footer{position:absolute;left:0;top:3201px;width:1200px;height:399px;background:var(--footer);color:#d9d2c6}
.foot-brand{position:absolute;left:500px;top:76px;width:200px;text-align:center;color:var(--gold);font-family:"Libre Baskerville",serif;font-size:16px;letter-spacing:5px}
.foot-mark{position:absolute;left:588px;top:44px;width:24px;height:24px;border:1.5px solid var(--gold)}
.foot-brand small{display:block;font-size:8px;letter-spacing:4px;margin-top:3px}
.foot-links{position:absolute;left:343px;top:170px;list-style:none;font-size:11px;letter-spacing:1px;line-height:18px}
.foot-contact{position:absolute;left:496px;font-size:10.5px;letter-spacing:1px;display:flex;align-items:center;gap:10px}
.social{position:absolute;top:256px;width:20px;height:20px;border:1.5px solid var(--gold)}
.badge{position:absolute;left:755px;top:174px;width:100px;height:100px;border-radius:50%;background:#f2e58c;border:3px solid #e6d35b}
.copy{position:absolute;top:332px;width:1200px;text-align:center;font-size:10px;letter-spacing:1.3px}
</style>
</head>
<body>

<header class="hero">
  <div class="photo hero-couple" role="img" aria-label="Bride and groom kissing beside a lake at dusk"></div>
  <nav class="nav">
    <a style="left:263px">FILMS</a>
    <a style="left:347px">PRICES</a>
    <a style="left:439px">REVIEWS</a>
    <div class="brand">BDMR<small>WEDDING FILMS</small></div>
    <a style="left:702px">OPTIONS</a>
    <a style="left:807px">ABOUT</a>
    <a style="left:899px">CONTACT</a>
  </nav>
  <div class="hero-title">
    <div class="frame"></div>
    <h1 class="serif">WEDDING FILMS</h1>
    <p class="serif">NORTH EAST, UK AND<br>WORLDWIDE FILMS</p>
  </div>
</header>

<section class="intro">
  <p class="abs eyebrow">BDMR<br>WEDDING FILMS</p>
  <h2 class="abs serif intro-h">YOUR VERY OWN<br>TIME CAPSULE</h2>
  <p class="abs intro-p">BDMR is a wedding filmmaker based in the north east of England. We film weddings in a fun and natural way. All weddings are totally unique to the couple. If you are looking for a wedding film for your special day we'd love to hear from you.</p>
  <div class="btn" style="left:126px;top:1042px;width:163px;height:44px">LEARN MORE <span>&rarr;</span></div>
  <div class="photo" style="left:587px;top:750px;width:525px;height:337px;background:linear-gradient(160deg,#b59f86 0%,#e9e1d4 40%,#f7f5f1 65%,#8a7a68 100%)" role="img" aria-label="Couple walking back down the church aisle after the ceremony"></div>
  <div class="photo" style="left:475px;top:715px;width:225px;height:225px;background:linear-gradient(135deg,#4d4741 0%,#7d7368 50%,#3a3632 100%)" role="img" aria-label="Film still of couple about to kiss"></div>
  <div class="play" style="left:563px;top:806px"></div>
</section>

<section class="grid">
  <div class="tile" style="left:0;top:1162px;background:linear-gradient(160deg,#8e9a8a,#e8e6e0 55%,#5c5a58)" role="img" aria-label="Bride with bouquet beside groom in checked suit"></div>
  <div class="tile feature" style="left:300px;top:1162px">
    <div class="frame"></div>
    <h3 class="serif">HATTIE &amp; OWEN</h3>
    <p>LARKFIELD HALL WEDDING</p>
  </div>
  <div class="tile" style="left:600px;top:1162px;background:linear-gradient(160deg,#5b6a5c,#2d3330 55%,#d9d6d0)" role="img" aria-label="Couple among cypress trees at a garden venue"></div>
  <div class="tile" style="left:900px;top:1162px;background:linear-gradient(160deg,#6b5a3c,#c8a16e 50%,#2b3145)" role="img" aria-label="Couple touching foreheads at golden hour"></div>
  <div class="tile" style="left:0;top:1462px;background:linear-gradient(160deg,#6b5548,#a48a76 50%,#3b302b)" role="img" aria-label="Couple embracing cheek to cheek"></div>
  <div class="tile" style="left:300px;top:1462px;background:linear-gradient(160deg,#59704e,#eceae5 50%,#23262b)" role="img" aria-label="Couple under falling confetti"></div>
  <div class="tile" style="left:600px;top:1462px;background:linear-gradient(160deg,#c9b9a6,#495677 50%,#efe8df)" role="img" aria-label="Couple kissing at the altar"></div>
  <div class="tile" style="left:900px;top:1462px;background:linear-gradient(160deg,#a5abb0,#b4705a 50%,#6e7b8c)" role="img" aria-label="Bride in flower crown beside groom by the coast"></div>
</section>

<section class="alt">
  <h2 class="section-h serif" style="top:82px;font-size:22px">PREFER SOMETHING A BIT MORE FUNKY?</h2>
  <p class="section-sub" style="top:116px">IF YOU ARE A COUPLE WHO PREFERS SOMETHING A BIT DIFFERENT TO THE<br>STYLES ABOVE THEN WHY NOT GO FOR OUR ALTERNATIVE OPTION.</p>

  <div class="photo" style="left:0;top:223px;width:98px;height:162px;background:linear-gradient(135deg,#7a6a5c,#e3dcd2)" role="img" aria-label="Couple kissing film still"></div>
  <p class="card-place" style="left:-6px;top:410px">H YORKSHIRE</p>

  <div class="photo" style="left:100px;top:223px;width:269px;height:162px;background:linear-gradient(150deg,#54704a,#ecebe6 50%,#222428)" role="img" aria-label="Couple under confetti film still"></div>
  <p class="card-name" style="left:122px;top:400px">MEGAN &amp; LUKE</p>
  <p class="card-place" style="left:122px;top:427px">ASHBY GRANGE, NORTH YORKSHIRE</p>

  <div class="photo" style="left:370px;top:187px;width:425px;height:239px;background:linear-gradient(150deg,#8b8a6e,#d6cbb8 45%,#6b6a5e)" role="img" aria-label="Couple showered with petals as they leave the ceremony"></div>
  <div class="play" style="left:558px;top:283px"></div>
  <p class="card-name" style="left:392px;top:444px;font-size:17px">MEGAN &amp; LUKE</p>
  <p class="card-place" style="left:392px;top:474px;font-size:11px">ASHBY GRANGE, NORTH YORKSHIRE</p>

  <div class="photo" style="left:796px;top:223px;width:268px;height:162px;background:linear-gradient(180deg,#dfe3e2,#5b7452 45%,#8a78a8 75%,#6a5f86)" role="img" aria-label="Couple standing in a lavender field"></div>
  <p class="card-name" style="left:817px;top:400px">MEGAN &amp; LUKE</p>
  <p class="card-place" style="left:817px;top:427px">ASHBY GRANGE, NORTH YORKSHIRE</p>

  <div class="photo" style="left:1066px;top:223px;width:134px;height:162px;background:linear-gradient(150deg,#3f4c3a,#2c3347 50%,#e9e3db)" role="img" aria-label="Couple embracing outdoors"></div>
  <p class="card-name" style="left:1087px;top:400px;white-space:nowrap">MEGAN &amp; LUKE</p>
  <p class="card-place" style="left:1087px;top:427px;white-space:nowrap">ASHBY GRANGE, NORTH YORKSHIRE</p>
</section>

<section class="reviews">
  <h2 class="section-h serif" style="top:2415px;font-size:24px">KIND WORDS.</h2>
  <p class="section-sub" style="top:2450px">WHAT IS DONE IN LOVE, IS DONE WELL.</p>
  <div class="photo" style="left:263px;top:2498px;width:673px;height:222px;background:linear-gradient(120deg,#c9a98a,#f1ebe2 30%,#3f4a66 50%,#efe9e2 68%,#d7a9a3 100%)" role="img" aria-label="Couple kissing during the ceremony"></div>
  <div class="review-tag">CHLOE &amp; JAMES</div>
  <p class="abs review-text">Absolutely amazing videographer! What can we say, our short film captures our day perfectly and includes everything we wanted. Both Daniel and Rowan were most professional and easy to work with on the day. They captured moments that I wouldn't have seen otherwise (like groom panicking beforehand). Would highly recommend!</p>
  <div class="abs dots"><i></i><i></i><i></i><i></i><i></i></div>
  <div class="btn" style="left:513px;top:2864px;width:176px;height:42px">SEE ALL REVIEWS <span>&rarr;</span></div>
</section>

<section class="feed">
  <h4>FOLLOW US ON @bdmrfilms</h4>
  <div class="thumb" style="left:172px;background:linear-gradient(135deg,#2b2c3a,#c9b8a0)" role="img" aria-label="Social post: evening reception"></div>
  <div class="thumb" style="left:279px;background:linear-gradient(135deg,#7c8580,#2e3138)" role="img" aria-label="Social post: guests outside venue"></div>
  <div class="thumb" style="left:387px;background:linear-gradient(135deg,#8fa0ad,#c97c5c)" role="img" aria-label="Social post: outdoor ceremony"></div>
  <div class="thumb" style="left:494px;background:linear-gradient(135deg,#3a2a22,#8b6a55)" role="img" aria-label="Social post: close detail shot"></div>
  <div class="thumb" style="left:602px;background:linear-gradient(135deg,#6f8a5a,#d98aa0)" role="img" aria-label="Social post: bouquet and confetti"></div>
  <div class="thumb" style="left:709px;background:linear-gradient(135deg,#a7a9b3,#7a6c90)" role="img" aria-label="Social post: groom's suit detail"></div>
  <div class="thumb" style="left:817px;background:linear-gradient(135deg,#c9a57e,#3c3f5a)" role="img" aria-label="Social post: couple at the altar"></div>
  <div class="thumb" style="left:924px;background:linear-gradient(135deg,#8fb2cf,#e6c9b4)" role="img" aria-label="Social post: bride getting ready"></div>
</section>

<footer class="footer">
  <div class="foot-mark"></div>
  <div class="foot-brand">BDMR<small>WEDDING FILMS</small></div>
  <ul class="foot-links">
    <li>› HOME</li><li>› FILMS</li><li>› PRICES</li><li>› REVIEWS</li><li>› OPTIONS</li><li>› ABOUT</li><li>› CONTACT</li>
  </ul>
  <div class="foot-contact" style="top:174px">
    <svg width="14" height="14" viewBox="0 0 14 14" fill="none" stroke="#9d864c" stroke-width="1.2"><path d="M3 1.5l2 2.5-1.2 1.5c.8 1.8 2 3 3.8 3.8l1.5-1.2 2.5 2-1.2 1.9C6 11.8 2.2 8 1.2 2.7z"/></svg>
    07000 123 456
  </div>
  <div class="foot-contact" style="top:208px">
    <svg width="14" height="11" viewBox="0 0 14 11" fill="none" stroke="#9d864c" stroke-width="1.2"><rect x=".6" y=".6" width="12.8" height="9.8"/><path d="M.6 .6L7 6l6.4-5.4"/></svg>
    FILMS@BDMRFILMS.COM
  </div>
  <div class="social" style="left:496px" role="img" aria-label="Social link one"></div>
  <div class="social" style="left:529px" role="img" aria-label="Social link two"></div>
  <div class="social" style="left:562px" role="img" aria-label="Social link three"></div>
  <div class="badge" role="img" aria-label="Featured-in badge"></div>
  <p class="copy">COPYRIGHT © 2020 BDMR FILMS LIMITED ALL RIGHTS RESERVED.</p>
</footer>

</body>
</html>
```